Concierge Healthcare Business Card Design and Logo

We need a logo and business card design for a new company called "Sound Harbor". We will provide concierge audiological care, hearing aids, hearing exams, custom hearing protection etc to patients in the comfort of their homes and offices. We would like a sleek and modern design preferably with an Ear related logo.

Target Market(s)

People with hearing loss, Hunters, Musicians
My usual clientele are older individuals so usually 50+ years old

Industry/Entity Type

Health Care

Contact Information for Business Card

Delia Franks, AuD
Audiologist
512-648-2917
soundharbor@mailnest.com
www.soundharbor-example.com

Logo Text

Sound Harbor

Number of Pages Required

3 page

```html
<!DOCTYPE html>
<html lang="en">
<head>
<meta charset="utf-8">
<title>Sound Harbor Business Card</title>
<link href="https://fonts.googleapis.com/css2?family=Montserrat:wght@400;500;600&display=swap" rel="stylesheet">
<style>
  :root {
    --page-bg: #2b2b2d;
    --card-grey: #818285;
    --card-white: #ffffff;
    --brand-blue: #27aae1;
    --text-grey: #7a7b7e;
    --logo-grey: #8a8b8e;
  }
  * { margin: 0; padding: 0; box-sizing: border-box; }
  html, body {
    width: 1200px; height: 900px; overflow: hidden;
    background: var(--page-bg);
    font-family: "Montserrat", sans-serif;
  }
  .card {
    position: absolute;
    left: 280px;
    width: 640px; height: 366px;
    box-shadow: 0 10px 28px rgba(0,0,0,0.45);
  }
  .card-back { top: 48px; background: var(--card-grey); }
  .card-front { top: 470px; background: var(--card-white); }

  .brand {
    display: flex; align-items: center; gap: 14px;
  }
  .brand-dot {
    width: 46px; height: 46px; border-radius: 50%;
    flex: none;
  }
  .brand-name {
    font-weight: 600; letter-spacing: 3px; text-transform: uppercase;
  }

  .card-back .brand {
    position: absolute; left: 0; right: 0; top: 134px;
    justify-content: center;
  }
  .card-back .brand-dot { background: var(--brand-blue); }
  .card-back .brand-name { color: #ffffff; font-size: 34px; }
  .card-back .website {
    position: absolute; left: 0; right: 0; top: 208px;
    text-align: center; color: #ffffff; font-size: 15px; letter-spacing: 0.5px;
  }

  .card-front .brand { position: absolute; left: 48px; top: 62px; }
  .card-front .brand-dot { background: var(--logo-grey); }
  .card-front .brand-name { color: var(--brand-blue); font-size: 28px; }

  .holder { position: absolute; left: 48px; top: 162px; }
  .holder-name { color: var(--brand-blue); font-weight: 600; font-size: 19px; }
  .holder-title { color: var(--text-grey); font-size: 14px; margin-top: 2px; }

  .divider {
    position: absolute; left: 0; right: 0; top: 216px;
    height: 2px; background: var(--brand-blue);
  }

  .contacts {
    position: absolute; left: 48px; top: 234px;
    list-style: none; color: var(--text-grey); font-size: 14px;
  }
  .contacts li { display: flex; align-items: center; gap: 10px; height: 24px; }
  .contacts svg { width: 13px; height: 13px; flex: none; }
</style>
</head>
<body>

<section class="card card-back">
  <div class="brand">
    <span class="brand-dot"></span>
    <span class="brand-name">Sound Harbor</span>
  </div>
  <p class="website">www.soundharbor-example.com</p>
</section>

<section class="card card-front">
  <div class="brand">
    <span class="brand-dot"></span>
    <span class="brand-name">Sound Harbor</span>
  </div>

  <div class="holder">
    <p class="holder-name">Delia Franks, AuD</p>
    <p class="holder-title">Audiologist</p>
  </div>

  <div class="divider"></div>

  <ul class="contacts">
    <li>
      <svg viewBox="0 0 16 16" aria-hidden="true"><path fill="#27aae1" d="M3.6 1.2 6 3.6 4.7 5.4c.8 1.9 2.1 3.2 3.9 3.9l1.8-1.3 2.4 2.4-1.6 2.4C6.5 12.5 3.5 9.5 1.2 2.8z"/></svg>
      512-648-2917
    </li>
    <li>
      <svg viewBox="0 0 16 16" aria-hidden="true"><rect x="1.5" y="3.5" width="13" height="9" fill="none" stroke="#27aae1" stroke-width="1.6"/><path d="M1.5 3.5 8 9l6.5-5.5" fill="none" stroke="#27aae1" stroke-width="1.6"/></svg>
      soundharbor@mailnest.com
    </li>
    <li>
      <svg viewBox="0 0 16 16" aria-hidden="true"><circle cx="8" cy="8" r="6.5" fill="none" stroke="#27aae1" stroke-width="1.4"/><ellipse cx="8" cy="8" rx="2.8" ry="6.5" fill="none" stroke="#27aae1" stroke-width="1.2"/><path d="M1.5 8h13" stroke="#27aae1" stroke-width="1.2"/></svg>
      www.soundharbor-example.com
    </li>
  </ul>
</section>

</body>
</html>
```